Slider created for Warm Kettle Kitchen

We need a new slider created for our Warm Kettle Kitchen website (www.warmkettlekitchen.com.au). Warm Kettle Kitchen is a central place where people who love food, cooking for their family and sharing recipes can hang out. We'd like the sliders to look more 'earthy' than the ones currently used - and more like our Facebook style https://www.facebook.com/WarmKettleKitchen .
The first slider we'd like to create will point to the blog on the website with the following:
Text: In Season Now - Ruby Red Grapefruit
Image: Ruby Red Grapefruit
The slider is 990 X 225 pixels.

```html
<!DOCTYPE html>
<html lang="en">
<head>
<meta charset="utf-8">
<title>Warm Kettle Kitchen – In Season Now Slider</title>
<link rel="stylesheet" href="https://fonts.googleapis.com/css2?family=Montserrat:wght@300;400;600&family=Roboto+Slab:wght@300&display=swap">
<style>
  :root {
    --page-bg: #272727;
    --paper: #e8e4dd;
    --paper-light: #efece6;
    --ink: #3a3835;
    --rule: #8a8680;
    --accent-red: #d0121b;
    --white: #ffffff;
    --food-red: #b8261c;
    --food-deep: #6e1a12;
    --food-cream: #e9dcc0;
    --food-green: #8b9a5a;
  }
  * { margin: 0; padding: 0; box-sizing: border-box; }
  html, body {
    width: 1200px;
    height: 818px;
    overflow: hidden;
    background: var(--page-bg);
  }
  .stage {
    position: relative;
    width: 1200px;
    height: 818px;
  }
  .slider {
    position: absolute;
    left: 60px;
    top: 286px;
    width: 990px;
    height: 225px;
    transform: scale(1.0909);
    transform-origin: 0 0;
    overflow: hidden;
    background: radial-gradient(ellipse at 70% 40%, var(--paper-light) 0%, var(--paper) 70%);
  }
  .slider__photo {
    position: absolute;
    left: 0;
    top: 0;
    width: 600px;
    height: 225px;
    background:
      radial-gradient(circle at 12% 30%, var(--food-cream) 0%, transparent 18%),
      radial-gradient(circle at 30% 55%, var(--food-green) 0%, transparent 16%),
      radial-gradient(circle at 45% 25%, var(--food-cream) 0%, transparent 15%),
      radial-gradient(circle at 55% 65%, var(--food-red) 0%, transparent 22%),
      radial-gradient(circle at 22% 80%, var(--food-deep) 0%, transparent 20%),
      linear-gradient(100deg, var(--food-red) 0%, #c4432e 40%, var(--food-cream) 75%);
    -webkit-mask-image: linear-gradient(90deg, #000 78%, transparent 100%);
    mask-image: linear-gradient(90deg, #000 78%, transparent 100%);
  }
  .slider__copy {
    position: absolute;
    left: 568px;
    top: 50px;
    width: 387px;
    text-align: center;
  }
  .slider__kicker {
    display: flex;
    align-items: center;
    gap: 8px;
    font-family: "Roboto Slab", Georgia, serif;
    font-weight: 300;
    font-size: 21px;
    letter-spacing: 1.5px;
    color: var(--ink);
    text-transform: uppercase;
    line-height: 36px;
  }
  .slider__kicker::before,
  .slider__kicker::after {
    content: "";
    flex: 1;
    height: 1px;
    background: var(--rule);
  }
  .slider__title {
    font-family: "Montserrat", Arial, sans-serif;
    font-weight: 300;
    font-size: 36px;
    color: var(--accent-red);
    line-height: 44px;
    margin-top: 0;
    white-space: nowrap;
  }
  .slider__button {
    display: inline-block;
    margin-top: 17px;
    padding: 0 18px;
    height: 36px;
    line-height: 36px;
    background: var(--accent-red);
    color: var(--white);
    font-family: "Montserrat", Arial, sans-serif;
    font-weight: 600;
    font-size: 16px;
    border-radius: 2px;
    text-decoration: none;
  }
</style>
</head>
<body>
  <main class="stage">
    <section class="slider">
      <div class="slider__photo" role="img" aria-label="Close-up photo of a ruby red grapefruit salad with fennel, radish and black sesame seeds"></div>
      <div class="slider__copy">
        <p class="slider__kicker">In Season Now</p>
        <h1 class="slider__title">Ruby Red Grapefruit</h1>
        <a class="slider__button" href="#blog">Visit Blog</a>
      </div>
    </section>
  </main>
</body>
</html>
```